cosmetics need shampoo label of first product (hopefully many more to follow)

we are starting this new project with the creation of the first of a range of shampoos: Design of facing comprehend creation of logo and facing of the product, we want to achieve a brand recognition and facing that makes our product and product stand out, see briefing attached.

We want to have a degree of personality but also give a tone of professional brand.

If project takes off, then more product to design and more resources available.

Target Market(s)

consumer looking for a professional shampoo but not at hairdresser at convenient price and size (1 litre with pump) bottle of white plastic

Industry/Entity Type

Cosmetics

Colors
00a990

Requirements
Must have
• as this shampoo is for damaged hair, green colour is the one that symbolise this category see Velunore Fortique
• we want that the bottle stand out from the crowd and that people get that is a professional brand so the logo neoVita must be seen and the colour most make a difference in the shelves
Nice to have
• good balance between some personality and & professional
• not too white (as will not stand out in white products shelve) but not too colour as they may then merchandise in the shelve with coloured product
• big fonts easy to read
Should not have
• too clinical, to boring,

```html
<!DOCTYPE html>
<html lang="en">
<head>
<meta charset="utf-8">
<title>neoVita Repair Shampoo Label</title>
<link rel="stylesheet" href="https://fonts.googleapis.com/css2?family=Tenor+Sans&family=Arimo&display=swap">
<style>
  :root {
    --teal: #13a890;
    --olive: #4f6228;
    --ink: #111111;
    --paper: #ffffff;
    --rule: #333333;
  }
  * { margin: 0; padding: 0; box-sizing: border-box; }
  html, body {
    width: 1000px;
    height: 1200px;
    overflow: hidden;
    background: var(--paper);
  }
  .canvas {
    position: relative;
    width: 1000px;
    height: 1200px;
    background: var(--paper);
  }
  .label {
    position: absolute;
    left: 120px;
    top: 181px;
    width: 707px;
    height: 942px;
    border: 1px solid var(--rule);
    font-family: "Tenor Sans", sans-serif;
    color: var(--ink);
    text-align: center;
  }
  .brand {
    position: absolute;
    left: 0;
    right: 0;
    top: 150px;
    display: flex;
    flex-direction: column;
    align-items: center;
  }
  .brand-name {
    font-family: "Tenor Sans", sans-serif;
    font-size: 124px;
    line-height: 1;
    color: var(--teal);
    letter-spacing: 1px;
  }
  .brand-tagline {
    margin-top: 22px;
    font-size: 32px;
    letter-spacing: 2px;
    color: var(--olive);
    text-transform: uppercase;
  }
  .copy {
    position: absolute;
    left: 0;
    right: 0;
    font-variant: small-caps;
    font-size: 23px;
    letter-spacing: 1px;
    line-height: 28px;
  }
  .copy-en { top: 470px; }
  .copy-fr { top: 528px; }
  .copy-use { top: 610px; }
  .copy-claims { top: 775px; }
  .net-weight {
    position: absolute;
    left: 0;
    right: 0;
    top: 858px;
    font-family: "Arimo", sans-serif;
    font-size: 21px;
    color: var(--ink);
  }
</style>
</head>
<body>
<div class="canvas">
  <section class="label">
    <div class="brand">
      <div class="brand-name">neoVita</div>
      <div class="brand-tagline">Salon Formula</div>
    </div>

    <p class="copy copy-en">Repair shampoo with argan oil</p>
    <p class="copy copy-fr">Shampooing reparateur avec huile argain</p>
    <p class="copy copy-use">For weakened – damaged hair<br>Pour cheveux habimes et affaiblis</p>
    <p class="copy copy-claims">Parabens free – sls free – colour safe</p>

    <p class="net-weight">NET WT 33.8 fl oz e 1000 ml</p>
  </section>
</div>
</body>
</html>
```